300 x 250 Web Ad for Porn Website

300 x 250 web ad that will appear on a porn site. Need to see 3 options, one with each of the 3 girls. Remove the background around the girls.

Underneath the girls image should read in big bold letters: High Speed Internet
Underneath in slightly smaller size: NO Credit Check

To the left of the girl: Save MONEY...

To the right of the girl: So you can buy more PORN

We want it to look very unique, raunchy, and eye catching.

Target Market(s)

Porn website

Industry/Entity Type

Internet Service Provider

Colors

Designer to choose colors to be used in the design.

Requirements
Must have
• Must stand out so people will definitely notice it.
• JPEG and PNG formats

```html
<!DOCTYPE html>
<html lang="en">
<head>
<meta charset="UTF-8">
<title>High Speed Internet – 300x250 Banner Set</title>
<link href="https://fonts.googleapis.com/css2?family=Roboto+Slab:wght@400;500&family=Russo+One&family=Yanone+Kaffeesatz:wght@600;700&family=Open+Sans:wght@500&display=swap" rel="stylesheet">
<style>
  :root {
    --board-bg: #ececec;
    --board-streak: #dcdcdc;
    --ink: #111111;
    --banner-black: #050505;
    --banner-red: #b30000;
    --speed-red: #e10000;
    --white: #ffffff;
    --band-grey: #6e6e6e;
    --promo-yellow: #f4e600;
    --gauge-dark: #2a2a2a;
    --gauge-light: #d9d9d9;
  }
  * { margin: 0; padding: 0; box-sizing: border-box; }
  html, body { width: 1200px; height: 1000px; overflow: hidden; }
  body {
    position: relative;
    background:
      repeating-linear-gradient(90deg, transparent 0 37px, var(--board-streak) 37px 38px, transparent 38px 83px),
      var(--board-bg);
    font-family: "Open Sans", sans-serif;
    color: var(--ink);
  }

  .sheet-title {
    position: absolute; left: 0; width: 1200px; text-align: center;
    font-family: "Roboto Slab", serif;
  }
  .sheet-title--label { top: 58px; font-size: 42px; font-weight: 400; letter-spacing: 1px; }
  .sheet-title--size { top: 122px; font-size: 58px; font-weight: 400; letter-spacing: 2px; }

  .banner {
    position: absolute; top: 245px; width: 300px; height: 250px;
    overflow: hidden; border: 1px solid #222;
    background:
      radial-gradient(ellipse at 95% 20%, var(--banner-red) 0%, rgba(179,0,0,.5) 35%, transparent 65%),
      var(--banner-black);
  }
  .banner--one { left: 111px; }
  .banner--two { left: 438px; }
  .banner--three { left: 764px; }

  .banner__headline {
    position: absolute; left: 6px;
    font-family: "Russo One", sans-serif; font-style: normal;
    transform: skewX(-12deg); white-space: nowrap; line-height: 1;
  }
  .banner__headline--speed { top: 10px; font-size: 28px; color: var(--speed-red); }
  .banner__headline--net { top: 41px; left: 24px; font-size: 28px; color: var(--white); }
  .banner__credit {
    position: absolute; top: 75px; left: 46px;
    font-size: 11.5px; color: var(--white); letter-spacing: .3px;
  }
  .banner__band {
    position: absolute; top: 93px; left: 0; width: 300px; height: 46px;
    background: linear-gradient(90deg, var(--band-grey), #8a8a8a 70%, #5a5a5a);
  }
  .banner__promo {
    position: absolute; left: 8px;
    font-family: "Yanone Kaffeesatz", sans-serif; font-weight: 700;
    color: var(--promo-yellow); white-space: nowrap; line-height: 1;
  }
  .banner__promo--save { top: 97px; font-size: 19px; font-style: italic; }
  .banner__promo--buy { top: 118px; font-size: 16px; color: var(--white); }
  .banner__promo--buy strong { color: var(--promo-yellow); font-size: 18px; }

  .banner__gauge {
    position: absolute; left: -20px; top: 150px; width: 240px; height: 200px;
    border-radius: 50%;
    background: radial-gradient(circle at 45% 45%, #ffffff 0%, #e8e8e8 45%, var(--gauge-dark) 62%, #9a9a9a 70%, #3a3a3a 78%);
  }
  .banner__model {
    position: absolute; top: 0; height: 250px;
    background: linear-gradient(180deg, #5b3b2c 0%, #a4735a 40%, #2a1a14 100%);
    border-radius: 40% 40% 10% 10%;
  }
  .banner--one .banner__model { left: 168px; width: 130px; }
  .banner--two .banner__model { left: 0; width: 110px; background: linear-gradient(180deg, #2a1b16 0%, #b88f82 45%, #7a574b 100%); }
  .banner--three .banner__model { left: 182px; width: 118px; background: linear-gradient(180deg, #3a2520 0%, #c48f73 40%, #a31d2a 75%, #6a3b2e 100%); }

  .banner--two .banner__headline--speed { left: 100px; }
  .banner--two .banner__headline--net { left: 118px; }
  .banner--two .banner__credit { left: 142px; }
  .banner--two .banner__promo { left: 124px; }
  .banner--two .banner__gauge { left: 90px; }

  .hero-gauge {
    position: absolute; left: -180px; top: 610px; width: 840px; height: 840px;
    border-radius: 50%;
    background: radial-gradient(circle at 50% 50%, #ffffff 0%, #f1f1f1 38%, var(--gauge-light) 44%, var(--gauge-dark) 47%, #4a4a4a 53%, #bdbdbd 56%, #6a6a6a 60%, #2b2b2b 64%, transparent 65%);
  }

  .hero-headline {
    position: absolute; right: 40px; text-align: right;
    font-family: "Russo One", sans-serif; line-height: 1;
    transform: skewX(-14deg); white-space: nowrap;
  }
  .hero-headline--speed { top: 765px; font-size: 78px; color: var(--speed-red); right: 38px; }
  .hero-headline--net { top: 845px; font-size: 78px; color: var(--ink); right: 82px; }
</style>
</head>
<body>
  <h1 class="sheet-title sheet-title--label">BANNER SIZE</h1>
  <p class="sheet-title sheet-title--size">300X250</p>

  <section class="banner banner--one">
    <div class="banner__gauge" role="img" aria-label="Internet speed gauge with needle near maximum"></div>
    <div class="banner__band"></div>
    <p class="banner__headline banner__headline--speed">HIGH SPEED</p>
    <p class="banner__headline banner__headline--net">INTERNET</p>
    <p class="banner__credit">NO CREDIT CHECK</p>
    <p class="banner__promo banner__promo--save">SAVE MONEY...</p>
    <p class="banner__promo banner__promo--buy">So you can buy <strong>MORE PORN</strong></p>
    <div class="banner__model" role="img" aria-label="Cut-out photo of a model in a black bikini"></div>
  </section>

  <section class="banner banner--two">
    <div class="banner__gauge" role="img" aria-label="Internet speed gauge with needle near maximum"></div>
    <div class="banner__band"></div>
    <p class="banner__headline banner__headline--speed">HIGH SPEED</p>
    <p class="banner__headline banner__headline--net">INTERNET</p>
    <p class="banner__credit">NO CREDIT CHECK</p>
    <p class="banner__promo banner__promo--save">SAVE MONEY...</p>
    <p class="banner__promo banner__promo--buy">So you can buy <strong>MORE PORN</strong></p>
    <div class="banner__model" role="img" aria-label="Cut-out photo of a model in a sheer bodysuit"></div>
  </section>

  <section class="banner banner--three">
    <div class="banner__gauge" role="img" aria-label="Internet speed gauge with needle near maximum"></div>
    <div class="banner__band"></div>
    <p class="banner__headline banner__headline--speed">HIGH SPEED</p>
    <p class="banner__headline banner__headline--net">INTERNET</p>
    <p class="banner__credit">NO CREDIT CHECK</p>
    <p class="banner__promo banner__promo--save">SAVE MONEY...</p>
    <p class="banner__promo banner__promo--buy">So you can buy <strong>MORE PORN</strong></p>
    <div class="banner__model" role="img" aria-label="Cut-out photo of a model in red lingerie and a fur coat"></div>
  </section>

  <div class="hero-gauge" role="img" aria-label="Large internet speed gauge reading slow, normal, fast, maximum with the needle in the red zone"></div>

  <p class="hero-headline hero-headline--speed">HIGH SPEED</p>
  <p class="hero-headline hero-headline--net">INTERNET</p>
</body>
</html>
```